TRELUDAX.live*

I am needing a web site built for the main purpose of uploading podcasts
(MP3 files) to be viewed by large audiences of 1000+ site visitors on a regular basis. I have created a rough draft of how I want the site to look.

i have created a rough draft of the home page - the LOGO for this site is a spectacular lightening bolt which appears on my home page sample... the file for this image I purchased is too large to download to your site. I will supply on reuquest.

There will be 5 pages; HOME ABOUT RESOURCES DEVOTIONALS GLENN.
I have all the content prepared for each of the above pages.

Target Market(s)

All people groups seeking positive and encouraging words, life lessons and testimonies of faith.

Coding

Coded - Design and coding required

Number of Pages Required

1 page

Colors
3176b5

Requirements
Must have
• The design and layout provided - my sample

Black backgrounds as shown on my sample

```html
<!DOCTYPE html>
<html lang="en">
<head>
<meta charset="utf-8">
<title>TRELUDAX.live – The Life Changing Podcasts</title>
<link rel="stylesheet" href="https://fonts.googleapis.com/css2?family=Hanken+Grotesk:wght@400;500;600;700&display=swap">
<style>
  :root {
    --brand: #3176b5;
    --button: #0b76c0;
    --dark: #2b2b2e;
    --footer: #23242b;
    --card: #2d2d30;
    --white: #ffffff;
    --ink: #1d1d1f;
    --muted: #c9c9cf;
  }
  * { box-sizing: border-box; margin: 0; padding: 0; }
  html, body { width: 1200px; height: 2461px; overflow: hidden; }
  body { font-family: "Hanken Grotesk", Arial, sans-serif; background: var(--white); color: var(--ink); position: relative; }
  a { color: inherit; text-decoration: none; }

  .top-strip { position: absolute; top: 0; left: 0; width: 1200px; height: 6px; background: var(--brand); z-index: 3; }

  .hero { position: absolute; top: 0; left: 0; width: 1200px; height: 594px; background: var(--dark);
    clip-path: polygon(0 0, 100% 0, 100% 489px, 0 594px); }
  .hero-glow { position: absolute; left: 260px; top: 90px; width: 300px; height: 400px;
    background: radial-gradient(ellipse at 50% 45%, rgba(70,110,255,.45), rgba(40,200,230,.18) 40%, rgba(43,43,46,0) 70%); }

  .site-nav { position: absolute; top: 12px; left: 160px; width: 880px; height: 30px; display: flex; align-items: center; z-index: 2; }
  .brand-name { font-size: 26px; font-weight: 700; color: var(--brand); letter-spacing: .5px; }
  .nav-links { margin-left: auto; display: flex; align-items: center; gap: 20px; font-size: 10px; color: var(--white); }
  .nav-subscribe { background: var(--button); border-radius: 10px; padding: 5px 9px; font-size: 10px; margin-left: 0; }

  .hero-copy { position: absolute; left: 161px; top: 104px; width: 480px; color: var(--white); z-index: 2; }
  .hero-kicker { color: var(--brand); font-size: 29px; font-weight: 400; }
  .hero-title { font-size: 55px; font-weight: 700; line-height: 76px; margin-top: 8px; letter-spacing: -.5px; }
  .hero-text { font-size: 18px; line-height: 30px; margin-top: 4px; width: 430px; }

  .host-photo { position: absolute; left: 666px; top: 67px; width: 384px; height: 480px; z-index: 2;
    background: linear-gradient(180deg, #2a2a30 0%, #25252a 60%, #3a2a22 100%);
    box-shadow: 0 4px 12px rgba(0,0,0,.35); }

  .episodes-kicker { position: absolute; left: 159px; top: 638px; color: var(--brand); font-size: 17px; }
  .episodes-title { position: absolute; left: 159px; top: 663px; font-size: 29px; font-weight: 700; color: var(--ink); }

  .episode-grid { position: absolute; left: 160px; top: 736px; width: 880px; display: grid;
    grid-template-columns: repeat(3, 280px); column-gap: 19px; row-gap: 26px; }
  .episode-card { height: 324px; background: var(--card); border-radius: 4px; overflow: hidden; position: relative;
    box-shadow: 0 2px 6px rgba(0,0,0,.25); color: var(--white); }
  .episode-art { height: 188px; }
  .art-yellow { background: linear-gradient(135deg, #f6d23a, #f2bd12 60%, #e8a90a); }
  .art-violet { background: linear-gradient(180deg, #6a4a6e 0%, #8a6b8c 60%, #ece8ee 100%); }
  .art-night { background: radial-gradient(ellipse at 40% 60%, #1f4cff 0%, #0a1a6a 25%, #040818 65%); }
  .art-studio { background: linear-gradient(90deg, #d9d6d2 0%, #bfb8b0 45%, #7f98ad 75%, #3f6f9c 100%); }
  .episode-number { position: absolute; top: 0; left: 0; background: var(--card); font-size: 11px; letter-spacing: 1.5px;
    padding: 3px 17px 4px 17px; }
  .episode-number span { border-bottom: 1px solid var(--brand); }
  .episode-body { padding: 9px 20px 0 20px; }
  .episode-meta { font-size: 7px; letter-spacing: .5px; display: flex; align-items: center; gap: 5px; }
  .episode-headline { font-size: 15.5px; font-weight: 600; letter-spacing: 1.4px; line-height: 19px; margin-top: 9px; }
  .episode-tags { font-size: 7px; letter-spacing: .5px; display: flex; align-items: center; gap: 5px; margin-top: 12px; }

  .btn-all { position: absolute; left: 531px; top: 1454px; width: 138px; height: 37px; background: var(--button); color: var(--white);
    font-size: 15px; display: flex; align-items: center; justify-content: center; border-radius: 2px; }

  .signup { position: absolute; left: 0; top: 1602px; width: 1200px; height: 504px; color: var(--white); text-align: center;
    background: radial-gradient(ellipse at 70% 55%, #3a3a3e 0%, #242427 55%, #1e1e21 100%); }
  .signup-title { position: absolute; left: 300px; top: 57px; width: 600px; font-size: 43px; font-weight: 700; line-height: 38px; letter-spacing: -.5px; }
  .signup-text { position: absolute; left: 310px; top: 199px; width: 580px; font-size: 18px; line-height: 23px; }
  .signup-field { position: absolute; left: 385px; width: 431px; height: 43px; background: var(--white); border: none; border-radius: 3px;
    font-family: inherit; font-size: 18px; padding: 0 13px; color: #999; text-align: left; display: flex; align-items: center; }
  .field-name { top: 296px; }
  .field-email { top: 359px; }
  .signup-submit { position: absolute; left: 385px; top: 422px; width: 431px; height: 43px; background: var(--button); color: var(--white);
    border-radius: 3px; font-size: 18px; display: flex; align-items: center; justify-content: center; }

  .site-footer { position: absolute; left: 0; top: 2106px; width: 1200px; height: 355px; background: var(--footer); color: var(--white); }
  .social-row { position: absolute; top: 64px; left: 469px; display: flex; gap: 38px; }
  .social-dot { width: 36px; height: 36px; border-radius: 50%; background: var(--white); display: block; }
  .footer-links { position: absolute; top: 142px; left: 0; width: 1200px; display: flex; justify-content: center; gap: 22px; font-size: 11px; }
  .copyright { position: absolute; top: 227px; left: 0; width: 1200px; text-align: center; font-size: 11px; letter-spacing: 1.2px; }
</style>
</head>
<body>
  <div class="top-strip"></div>

  <section class="hero">
    <div class="hero-glow" role="img" aria-label="Glowing blue lightning bolt behind the headline"></div>
  </section>

  <header class="site-nav">
    <a class="brand-name" href="#">TRELUDAX.live</a>
    <nav class="nav-links">
      <a href="#">Home</a>
      <a href="#">About</a>
      <a href="#">Resources</a>
      <a href="#">Devotionals</a>
      <a href="#">Glenn</a>
      <a class="nav-subscribe" href="#">Subscribe Now</a>
    </nav>
  </header>

  <div class="hero-copy">
    <p class="hero-kicker">Welcome to</p>
    <h1 class="hero-title">The Life Changing Podcasts</h1>
    <p class="hero-text">Lorem ipsum dolor sit amet, consectetur adipiscing elit, sed do eiusmod tempor incididunt ut labore et dolore magna aliqua. Quis ipsum suspendisse ultrices gravida. Risus commodo viverra maecenas accumsan lacus vel facilisis.</p>
  </div>

  <div class="host-photo" role="img" aria-label="Portrait of the podcast host in a black t-shirt with arms crossed, seated by a motorcycle"></div>

  <p class="episodes-kicker">LATEST EPISODES</p>
  <h2 class="episodes-title">See What’s New</h2>

  <div class="episode-grid">
    <article class="episode-card">
      <div class="episode-art art-yellow" role="img" aria-label="Black headphones on a yellow background"></div>
      <div class="episode-number"><span>Ep. 01</span></div>
      <div class="episode-body">
        <p class="episode-meta"><svg width="9" height="9" viewBox="0 0 10 10"><circle cx="5" cy="5" r="4" fill="none" stroke="#fff" stroke-width="1"/><path d="M5 2.5V5l2 1" fill="none" stroke="#fff" stroke-width="1"/></svg>15 hours ago</p>
        <h3 class="episode-headline">Lorem ipsum dolor sit amet, consectetur adipelit, sed do eiusmod tempor ut labore et</h3>
        <p class="episode-tags"><svg width="11" height="11" viewBox="0 0 12 12"><path d="M6.5 1H11v4.5L5.5 11 1 6.5z" fill="none" stroke="#fff" stroke-width="1"/><circle cx="8.7" cy="3.3" r=".9" fill="#fff"/></svg>Be you, tag list, why, Important talk</p>
      </div>
    </article>
    <article class="episode-card">
      <div class="episode-art art-violet" role="img" aria-label="Vintage studio microphone in violet light"></div>
      <div class="episode-number"><span>Ep. 02</span></div>
      <div class="episode-body">
        <p class="episode-meta"><svg width="9" height="9" viewBox="0 0 10 10"><circle cx="5" cy="5" r="4" fill="none" stroke="#fff" stroke-width="1"/><path d="M5 2.5V5l2 1" fill="none" stroke="#fff" stroke-width="1"/></svg>15 hours ago</p>
        <h3 class="episode-headline">Lorem ipsum dolor sit amet, consectetur adipelit, sed do eiusmod tempor ut labore et</h3>
        <p class="episode-tags"><svg width="11" height="11" viewBox="0 0 12 12"><path d="M6.5 1H11v4.5L5.5 11 1 6.5z" fill="none" stroke="#fff" stroke-width="1"/><circle cx="8.7" cy="3.3" r=".9" fill="#fff"/></svg>Be you, tag list, why, Important talk</p>
      </div>
    </article>
    <article class="episode-card">
      <div class="episode-art art-night" role="img" aria-label="Blue lightning bolt on a dark background"></div>
      <div class="episode-number"><span>Ep. 03</span></div>
      <div class="episode-body">
        <p class="episode-meta"><svg width="9" height="9" viewBox="0 0 10 10"><circle cx="5" cy="5" r="4" fill="none" stroke="#fff" stroke-width="1"/><path d="M5 2.5V5l2 1" fill="none" stroke="#fff" stroke-width="1"/></svg>15 hours ago</p>
        <h3 class="episode-headline">Lorem ipsum dolor sit amet, consectetur adipelit, sed do eiusmod tempor ut labore et</h3>
        <p class="episode-tags"><svg width="11" height="11" viewBox="0 0 12 12"><path d="M6.5 1H11v4.5L5.5 11 1 6.5z" fill="none" stroke="#fff" stroke-width="1"/><circle cx="8.7" cy="3.3" r=".9" fill="#fff"/></svg>Be you, tag list, why, Important talk</p>
      </div>
    </article>
    <article class="episode-card">
      <div class="episode-art art-night" role="img" aria-label="Blue lightning bolt on a dark background"></div>
      <div class="episode-number"><span>Ep. 04</span></div>
      <div class="episode-body">
        <p class="episode-meta"><svg width="9" height="9" viewBox="0 0 10 10"><circle cx="5" cy="5" r="4" fill="none" stroke="#fff" stroke-width="1"/><path d="M5 2.5V5l2 1" fill="none" stroke="#fff" stroke-width="1"/></svg>15 hours ago</p>
        <h3 class="episode-headline">Lorem ipsum dolor sit amet, consectetur adipelit, sed do eiusmod tempor ut labore et</h3>
        <p class="episode-tags"><svg width="11" height="11" viewBox="0 0 12 12"><path d="M6.5 1H11v4.5L5.5 11 1 6.5z" fill="none" stroke="#fff" stroke-width="1"/><circle cx="8.7" cy="3.3" r=".9" fill="#fff"/></svg>Be you, tag list, why, Important talk</p>
      </div>
    </article>
    <article class="episode-card">
      <div class="episode-art art-studio" role="img" aria-label="Blue condenser microphone on a stand in a studio"></div>
      <div class="episode-number"><span>Ep. 05</span></div>
      <div class="episode-body">
        <p class="episode-meta"><svg width="9" height="9" viewBox="0 0 10 10"><circle cx="5" cy="5" r="4" fill="none" stroke="#fff" stroke-width="1"/><path d="M5 2.5V5l2 1" fill="none" stroke="#fff" stroke-width="1"/></svg>15 hours ago</p>
        <h3 class="episode-headline">Lorem ipsum dolor sit amet, consectetur adipelit, sed do eiusmod tempor ut labore et</h3>
        <p class="episode-tags"><svg width="11" height="11" viewBox="0 0 12 12"><path d="M6.5 1H11v4.5L5.5 11 1 6.5z" fill="none" stroke="#fff" stroke-width="1"/><circle cx="8.7" cy="3.3" r=".9" fill="#fff"/></svg>Be you, tag list, why, Important talk</p>
      </div>
    </article>
    <article class="episode-card">
      <div class="episode-art art-yellow" role="img" aria-label="Black headphones on a yellow background"></div>
      <div class="episode-number"><span>Ep. 06</span></div>
      <div class="episode-body">
        <p class="episode-meta"><svg width="9" height="9" viewBox="0 0 10 10"><circle cx="5" cy="5" r="4" fill="none" stroke="#fff" stroke-width="1"/><path d="M5 2.5V5l2 1" fill="none" stroke="#fff" stroke-width="1"/></svg>15 hours ago</p>
        <h3 class="episode-headline">Lorem ipsum dolor sit amet, consectetur adipelit, sed do eiusmod tempor ut labore et</h3>
        <p class="episode-tags"><svg width="11" height="11" viewBox="0 0 12 12"><path d="M6.5 1H11v4.5L5.5 11 1 6.5z" fill="none" stroke="#fff" stroke-width="1"/><circle cx="8.7" cy="3.3" r=".9" fill="#fff"/></svg>Be you, tag list, why, Important talk</p>
      </div>
    </article>
  </div>

  <a class="btn-all" href="#">View All Episodes</a>

  <section class="signup" role="img" aria-label="Dark backdrop with headphones and a faint lightning bolt">
    <h2 class="signup-title">Get on the list for exclusive access to the private bonus feed.</h2>
    <p class="signup-text">Lorem ipsum dolor sit amet, consectetur adipiscing elit, sed do eiusmod tempor incididunt ut labore et dolore magna aliqua. Quis ipsum suspendisse ultrices gravida.</p>
    <div class="signup-field field-name">Your Name</div>
    <div class="signup-field field-email">Your Best Email Address</div>
    <div class="signup-submit">Submit</div>
  </section>

  <footer class="site-footer">
    <div class="social-row">
      <a class="social-dot" href="#" aria-label="Photo sharing profile"></a>
      <a class="social-dot" href="#" aria-label="Podcast listing"></a>
      <a class="social-dot" href="#" aria-label="Social network page"></a>
      <a class="social-dot" href="#" aria-label="Microblog profile"></a>
    </div>
    <nav class="footer-links">
      <a href="#">Home</a>
      <a href="#">About</a>
      <a href="#">Resources</a>
      <a href="#">Devotionals</a>
      <a href="#">Glenn</a>
    </nav>
    <p class="copyright">© TRELUDAX.LIVE</p>
  </footer>
</body>
</html>
```